Zielgruppe
Wir sind ein kleiner familiengeführter Weinbaubetrieb am Wagram und suchen einen modernen und naturnahen Namen und ein Etikett mit Blickfang für unseren Wermut, aus handgepflückten regionalen Wildkräutern mit Rosewein vom Zweigelt. Charakeristik des Getränks: Aperitif, Zitrusnote, leichte Bitternote, mit Tonic water als Cocktail.
Unsere Zielgruppe: kaufkräftige Genussmenschen im mittleren Alter
Aufgabenstellung
Etikett für 0,5l Flasche, Flasche noch nicht festgelegt, Etikettenhöhe: 65mm
Was soll draufstehen: Name, Vermouth, local botanicals, handcrafted, small batch

```html
<!DOCTYPE html>
<html lang="en">
<head>
<meta charset="utf-8">
<title>Sassolina Vermouth – Label</title>
<link rel="stylesheet" href="https://fonts.googleapis.com/css2?family=Fira+Sans:wght@300&family=Fira+Sans+Condensed:wght@400&family=Merriweather:wght@900&display=swap">
<style>
  :root {
    --backdrop: #e4e5ea;
    --label-red: #9e2424;
    --artwork-red: #a8302e;
    --artwork-deep: #9a2626;
    --cream: #f6e2b8;
    --paper: #f3dcb0;
    --ink: #0b0b0b;
  }
  html, body {
    margin: 0;
    padding: 0;
    width: 1200px;
    height: 1020px;
    overflow: hidden;
    background: var(--backdrop);
  }
  .label {
    position: absolute;
    left: 100px;
    top: 127px;
    width: 1000px;
    height: 765px;
    background: var(--paper);
    box-shadow: 0 6px 18px rgba(0,0,0,0.18);
    overflow: hidden;
  }
  .label__artwork {
    position: absolute;
    left: 0;
    top: 0;
    width: 1000px;
    height: 667px;
  }
  .label__brand {
    position: absolute;
    left: 200px;
    top: 0;
    width: 600px;
    height: 200px;
    margin: 0;
    background: var(--label-red);
    color: var(--cream);
    font-family: "Fira Sans", sans-serif;
    font-weight: 300;
    font-size: 110px;
    line-height: 200px;
    text-align: center;
    letter-spacing: 0;
    white-space: nowrap;
  }
  .label__product {
    position: absolute;
    left: 0;
    width: 1000px;
    top: 588px;
    margin: 0;
    color: var(--ink);
    font-family: "Merriweather", serif;
    font-weight: 900;
    font-size: 68px;
    line-height: 80px;
    text-align: center;
    letter-spacing: 2px;
  }
  .label__claims {
    position: absolute;
    left: 0;
    bottom: 0;
    width: 1000px;
    height: 98px;
    margin: 0;
    background: var(--ink);
    color: var(--cream);
    font-family: "Fira Sans Condensed", sans-serif;
    font-weight: 400;
    font-size: 39px;
    line-height: 98px;
    text-align: center;
    letter-spacing: 2.5px;
    white-space: nowrap;
  }
</style>
</head>
<body>
  <div class="label">
    <svg class="label__artwork" viewBox="0 0 1000 667" role="img" aria-label="Red halftone engraving of a lizard crawling diagonally across a sunlit stone">
      <defs>
        <linearGradient id="stone-tone" x1="0" y1="0" x2="1" y2="1">
          <stop offset="0" stop-color="#e7c39c"/>
          <stop offset="0.6" stop-color="#f1d6ad"/>
          <stop offset="1" stop-color="#ebc9a2"/>
        </linearGradient>
        <radialGradient id="shade-left" cx="0" cy="0.15" r="0.55">
          <stop offset="0" stop-color="#a52c2a"/>
          <stop offset="0.6" stop-color="#b5403a" stop-opacity="0.85"/>
          <stop offset="1" stop-color="#b5403a" stop-opacity="0"/>
        </radialGradient>
        <radialGradient id="shade-right" cx="1" cy="0.05" r="0.45">
          <stop offset="0" stop-color="#a52c2a"/>
          <stop offset="0.6" stop-color="#b23a36" stop-opacity="0.8"/>
          <stop offset="1" stop-color="#b23a36" stop-opacity="0"/>
        </radialGradient>
        <radialGradient id="body-tone" cx="0.5" cy="0.5" r="0.5">
          <stop offset="0" stop-color="#a8302e" stop-opacity="0.9"/>
          <stop offset="0.7" stop-color="#b5443c" stop-opacity="0.55"/>
          <stop offset="1" stop-color="#b5443c" stop-opacity="0"/>
        </radialGradient>
      </defs>
      <rect width="1000" height="667" fill="url(#stone-tone)"/>
      <rect width="1000" height="667" fill="url(#shade-left)"/>
      <rect width="1000" height="667" fill="url(#shade-right)"/>
      <ellipse cx="560" cy="410" rx="430" ry="150" transform="rotate(-28 560 410)" fill="url(#body-tone)"/>
    </svg>
    <h1 class="label__brand">SASSOLINA</h1>
    <p class="label__product">VERMOUTH</p>
    <p class="label__claims">LOCAL BOTANICALS - HANDCRAFTED - SMALL BATCH</p>
  </div>
</body>
</html>
```